New business card with our logo

we finalized our logo with the help of pixel harbor - now we need a business card using that logo. we are a metal service center providing raw steel and metal products for fabricating, contractors, artists, etc. we have the wording for the back of the card figured out (attached, no deviations from text please), just need help putting it all together.
would like the look of steel somehow incorporated in the design ... would like the black part of the logo to be steel or silver color (the S & BRANLEY)
Other font styles liked:
- calibri, arial, similar to those, modern looking
Colors
Designer to choose colors to be used in the design.
Requirements
Must have
- Back of card must haves are attached (no deviations from wording please).
- FRONT of card:
- logo
- address
- name
- office tel
- cell
- fax
- website
- address
Nice to have
- incorporate the look of steel or element of steel somehow
- names of the staff on front not in all caps, i.e. Rosvita not ROSVITA
- this industry is more industrial, not coffee or flower shop so design should be aligned with that
- design should be classic and tasteful

```html
<!DOCTYPE html>
<html lang="en">
<head>
<meta charset="utf-8">
<title>Branley Steel business card</title>
<link rel="stylesheet" href="https://fonts.googleapis.com/css2?family=Montserrat:wght@400;500;600;700&family=Open+Sans:wght@400;600&display=swap">
<style>
  :root {
    --bg: #2f2f31;
    --bg-edge: #1e1e20;
    --card-dark: #1b1b1d;
    --card-mid: #4a4a4e;
    --perf: #111113;
    --silver-hi: #f4f5f7;
    --silver: #c9ccd1;
    --silver-lo: #8d9096;
    --blue: #1f7fd1;
    --ink: #2b2d31;
    --ink-soft: #44474c;
    --white: #ffffff;
  }
  * { box-sizing: border-box; margin: 0; padding: 0; }
  html, body { width: 1200px; height: 900px; overflow: hidden; }
  body {
    background: radial-gradient(ellipse at 50% 45%, var(--bg) 0%, var(--bg-edge) 100%);
    font-family: "Open Sans", Arial, sans-serif;
    position: relative;
  }
  .card {
    position: absolute;
    top: 291px;
    width: 555px;
    height: 318px;
    border-radius: 4px;
    overflow: hidden;
    box-shadow: 0 12px 30px rgba(0,0,0,.55);
  }

  /* ---------- front ---------- */
  .card-front { left: 30px; background: var(--card-dark); }
  .perforated-band {
    position: absolute; left: 0; right: 0; height: 48px;
    background: linear-gradient(180deg, #1a1a1c, var(--perf));
  }
  .perforated-band.top { top: 0; }
  .perforated-band.bottom { bottom: 0; }
  .steel-strip {
    position: absolute; left: 0; right: 0; height: 12px;
    background: linear-gradient(180deg, var(--silver-lo), var(--silver-hi) 45%, var(--silver) 60%, var(--silver-lo));
  }
  .steel-strip.top { top: 48px; }
  .steel-strip.bottom { bottom: 48px; }
  .front-panel {
    position: absolute; left: 0; right: 0; top: 60px; bottom: 60px;
    background: radial-gradient(ellipse at 30% 40%, #6b6c70 0%, var(--card-mid) 30%, #222225 85%);
  }
  .front-brand {
    position: absolute; left: 34px; top: 38px;
    display: flex; align-items: center; gap: 14px;
  }
  .brand-dot {
    width: 50px; height: 50px; border-radius: 50%;
    background: var(--blue);
    flex: none;
  }
  .brand-name {
    font-family: "Montserrat", Arial, sans-serif;
    font-weight: 700;
    font-size: 30px;
    line-height: 1;
    letter-spacing: .5px;
  }
  .front-brand .brand-name { color: var(--white); }
  .divider {
    position: absolute; left: 262px; top: 26px; width: 2px; height: 146px;
    background: var(--silver);
    opacity: .85;
  }
  .contact {
    position: absolute; left: 286px; top: 20px;
    color: var(--white);
  }
  .contact-name {
    font-weight: 600; font-size: 25px; line-height: 1.1;
  }
  .contact-role { font-size: 13px; margin: 2px 0 8px; color: #e4e4e6; }
  .contact-list { list-style: none; }
  .contact-list li {
    display: flex; align-items: center; gap: 9px;
    font-size: 13.5px; line-height: 20px;
  }
  .contact-list svg { width: 12px; height: 12px; flex: none; }
  .address {
    position: absolute; left: 34px; bottom: 10px;
    color: var(--white); font-size: 12.5px;
  }

  /* ---------- back ---------- */
  .card-back {
    left: 615px;
    background: linear-gradient(125deg, #d6d9de 0%, var(--silver-hi) 28%, #b9bdc4 55%, #e9ebee 78%, #9ea2a9 100%);
  }
  .back-brand {
    position: absolute; left: 60px; top: 44px;
    display: flex; align-items: center; gap: 14px;
  }
  .back-brand .brand-name { color: var(--ink); font-size: 34px; }
  .back-brand .brand-dot { width: 54px; height: 54px; }
  .back-copy {
    position: absolute; left: 60px; right: 40px; top: 124px;
    font-family: "Montserrat", Arial, sans-serif;
  }
  .service-title {
    color: var(--blue); font-weight: 700; font-size: 23px; letter-spacing: .5px;
  }
  .service-actions {
    color: var(--ink-soft); font-weight: 500; font-size: 14px; letter-spacing: .6px;
    padding: 2px 0 7px;
    border-bottom: 1.5px solid var(--blue);
    width: 340px;
  }
  .service-lines { margin-top: 9px; color: var(--ink); font-size: 13px; font-weight: 500; line-height: 1.55; }
  .service-tagline { margin-top: 10px; color: var(--blue); font-size: 15px; font-weight: 500; }
</style>
</head>
<body>

<section class="card card-front" aria-label="Card front">
  <div class="perforated-band top" role="img" aria-label="Black perforated metal sheet texture"></div>
  <div class="steel-strip top"></div>
  <div class="front-panel">
    <div class="front-brand">
      <span class="brand-dot"></span>
      <span class="brand-name">BRANLEY<br>STEEL</span>
    </div>
    <div class="divider"></div>
    <div class="contact">
      <p class="contact-name">Dorian Kessler</p>
      <p class="contact-role">Director</p>
      <ul class="contact-list">
        <li><svg viewBox="0 0 12 12"><path d="M2.5 1h2l1 3-1.5 1a7 7 0 0 0 3 3l1-1.5 3 1v2a1 1 0 0 1-1 1A10 10 0 0 1 1.5 2a1 1 0 0 1 1-1z" fill="#fff"/></svg>+330 4172-3051</li>
        <li><svg viewBox="0 0 12 12"><rect x="3" y="0.5" width="6" height="11" rx="1.2" fill="none" stroke="#fff" stroke-width="1.2"/><circle cx="6" cy="9.5" r=".8" fill="#fff"/></svg>+330 4189-6624</li>
        <li><svg viewBox="0 0 12 12"><rect x="1" y="5" width="10" height="6" rx="1" fill="#fff"/><rect x="3" y="1" width="6" height="4" fill="none" stroke="#fff" stroke-width="1.2"/></svg>+330 4203-1187</li>
        <li><svg viewBox="0 0 12 12"><rect x="0.8" y="2.3" width="10.4" height="7.4" rx="1" fill="none" stroke="#fff" stroke-width="1.2"/><path d="M1 3l5 3.8L11 3" fill="none" stroke="#fff" stroke-width="1.2"/></svg>info@branleysteel.com</li>
        <li><svg viewBox="0 0 12 12"><circle cx="6" cy="6" r="5.2" fill="none" stroke="#fff" stroke-width="1.1"/><ellipse cx="6" cy="6" rx="2.3" ry="5.2" fill="none" stroke="#fff" stroke-width="1"/><path d="M1 6h10" stroke="#fff" stroke-width="1"/></svg>www.branleysteel.com</li>
      </ul>
    </div>
    <p class="address">5790 Alder Ridge Rd. Knoxville, TN 37919</p>
  </div>
  <div class="steel-strip bottom"></div>
  <div class="perforated-band bottom" role="img" aria-label="Black perforated metal sheet texture"></div>
</section>

<section class="card card-back" aria-label="Card back">
  <div class="back-brand">
    <span class="brand-dot"></span>
    <span class="brand-name">BRANLEY STEEL</span>
  </div>
  <div class="back-copy">
    <p class="service-title">METAL SERVICE CENTER</p>
    <p class="service-actions">CUT - SHEAR - PUNCH - LIGHT FAB</p>
    <p class="service-lines">Structural Steel - Stainless &amp; aluminm<br>Building Components - Rebar - Decking ...and more</p>
    <p class="service-tagline">Cut to size, Pick-up or Delivered!</p>
  </div>
</section>

</body>
</html>
```